Photographer website

This website will contain information to sell the services of marvello tebani an up and coming photographer based in london

Target Market(s)

SME's for corporate head shots
mums for kids parties
actors - for headshots
up and coming models

Industry/Entity Type

Photographer

Number of Pages Required

3 page

Requirements
Must have
• Home
• About me
• Contact me
• Portfolio or gallery

```html
<!DOCTYPE html>
<html lang="en">
<head>
<meta charset="utf-8">
<title>Velour Dark — Photography</title>
<link rel="stylesheet" href="https://fonts.googleapis.com/css2?family=PT+Sans:wght@400;700&family=Libre+Baskerville:wght@400;700&display=swap">
<style>
:root{
  --backdrop:#000;
  --page:#fff;
  --ink:#2b2b2b;
  --muted:#555;
  --rule:#bdbdbd;
  --footer:#222;
  --footer-text:#d8d8d8;
  --white:#fff;
  --btn:#000;
  --sans:"PT Sans", Arial, sans-serif;
  --serif:"Libre Baskerville", Georgia, serif;
}
*{box-sizing:border-box;margin:0;padding:0}
html,body{width:1200px;height:1200px;overflow:hidden;background:var(--backdrop)}
.canvas{position:relative;width:1200px;height:1200px;overflow:hidden}
.page{position:absolute;left:313px;top:0;width:719px;height:1500px;transform:scale(.8);transform-origin:0 0;background:var(--page);font-family:var(--sans);color:var(--ink)}

/* hero */
.hero{position:absolute;left:0;top:0;width:719px;height:340px;
  background:linear-gradient(180deg,#2d3540 0%,#48506a 22%,#9a8a70 38%,#4e5a3a 55%,#25301e 70%,#6c7d88 82%,#2b3128 100%)}
.masthead{position:absolute;left:0;top:0;width:719px;height:67px;background:rgba(20,24,30,.6)}
.brand{position:absolute;left:48px;top:22px;display:flex;align-items:center;gap:7px;color:var(--white);font-family:var(--sans);font-weight:700;font-size:15px;letter-spacing:1px}
.brand-dot{width:9px;height:9px;border-radius:50%;background:var(--white)}
.nav{position:absolute;top:32px;left:0;width:719px;list-style:none}
.nav li{position:absolute;color:var(--white);font-size:8.5px;font-weight:700;white-space:nowrap}
.hero-title{position:absolute;top:155px;left:0;width:719px;text-align:center;color:var(--white);font-family:var(--serif);font-weight:400;font-size:34px;letter-spacing:-.5px}
.hero-sub{position:absolute;top:198px;left:0;width:719px;text-align:center;color:#e8e8e8;font-family:var(--serif);font-size:11px}
.arrow{position:absolute;top:170px}

/* intro */
.intro{position:absolute;top:368px;left:30px;width:659px;text-align:center;font-size:12px;line-height:18px;color:var(--ink)}
.divider{position:absolute;top:422px;left:277px;width:165px;height:1px;background:var(--rule)}
.label{position:absolute;left:0;width:719px;text-align:center;font-size:7.5px;font-weight:700;letter-spacing:2px;color:var(--ink)}

/* gallery */
.gallery{position:absolute;top:467px;left:0;width:719px;height:650px;display:grid;grid-template-columns:240px 240px 239px;grid-template-rows:160px 164px 164px 163px}
.tile{position:relative;overflow:hidden}
.tile-title{position:absolute;left:10px;bottom:37px;color:var(--white);font-family:var(--serif);font-weight:400;font-size:12.5px;white-space:nowrap}
.tile-meta{position:absolute;left:10px;bottom:21px;color:#eee;font-family:var(--serif);font-size:7px;white-space:nowrap}
.tile-meta span{margin:0 7px}

/* collaborate */
.collab-text{position:absolute;top:1158px;left:60px;width:599px;text-align:center;font-size:8.5px;line-height:14px;color:var(--muted)}
.btn{position:absolute;top:1197px;left:320px;width:80px;height:17px;border-radius:9px;background:var(--btn);color:var(--white);font-size:7.5px;line-height:17px;text-align:center}

/* footer */
.footer{position:absolute;top:1246px;left:0;width:719px;height:254px;background:var(--footer);color:var(--footer-text);font-size:7.5px}
.col{position:absolute;top:34px}
.col h4{font-size:8px;font-weight:700;color:var(--white);margin-bottom:10px}
.post{position:relative;height:46px}
.thumb{position:absolute;left:0;top:0;width:38px;height:31px}
.post-title{position:absolute;left:46px;top:2px;font-size:7.5px;color:var(--white);white-space:nowrap}
.post-date{position:absolute;left:46px;top:20px;font-size:5.5px}
.cats{list-style:none;line-height:13.3px}
.cats li::before{content:"";display:inline-block;width:2.5px;height:2.5px;border-radius:50%;background:var(--white);margin:0 8px 2px 0}
.contact p{line-height:13.4px;white-space:nowrap}
.social{display:flex;gap:4px;margin-top:6px}
.social i{width:15px;height:15px;border-radius:50%;display:block}
.about-photo{width:145px;height:81px;background:linear-gradient(135deg,#6a7378,#3a4044 55%,#1c1f22)}
.about-text{margin-top:6px;line-height:13.3px;width:145px}
.copyright{position:absolute;top:223px;left:0;width:719px;text-align:center;font-size:7.5px;color:var(--footer-text)}
</style>
</head>
<body>
<div class="canvas">
<main class="page">

  <section class="hero" role="img" aria-label="Dusk landscape photo of white cliffs above a still lake reflecting the sky"></section>
  <header class="masthead">
    <div class="brand"><span class="brand-dot"></span>VELOUR DARK</div>
    <ul class="nav">
      <li style="left:327px">HOME</li>
      <li style="left:390px">ABOUT ME</li>
      <li style="left:466px">PORTFOLIO</li>
      <li style="left:545px">GALLERY</li>
      <li style="left:623px">CONTACT ME</li>
    </ul>
  </header>
  <h1 class="hero-title">LOREM IPSUM DOLOR</h1>
  <p class="hero-sub">Lorem ipsum dolor sit amet consectetur adipiscing</p>
  <svg class="arrow" style="left:26px" width="14" height="32" viewBox="0 0 14 32"><polyline points="12,2 3,16 12,30" fill="none" stroke="#ddd" stroke-width="2.5"/></svg>
  <svg class="arrow" style="left:681px" width="14" height="32" viewBox="0 0 14 32"><polyline points="2,2 11,16 2,30" fill="none" stroke="#ddd" stroke-width="2.5"/></svg>

  <p class="intro">Lorem ipsum dolor sit amet consectetur adipiscing elit. Aliquam venenatis nibh vitae consequat auctor. Ali<br>quam sed lorem tristique nisl egestas sollicitudin. Duis pulvinar vitae purus sed luctus Nulla aliquet</p>
  <div class="divider"></div>
  <p class="label" style="top:440px">ALL CATEGORIES</p>

  <section class="gallery">
    <article class="tile" role="img" aria-label="Woman in a red dress on a park bench" style="background:linear-gradient(135deg,#3b4a45,#5c5a4c 45%,#8a1e1e 70%,#2e2a24)"><h3 class="tile-title">Lorem ipsum dolor</h3><p class="tile-meta">7 PHOTOS<span>•</span>21 OCT 2016</p></article>
    <article class="tile" role="img" aria-label="Narrow cobbled old-town street with yellow buildings" style="background:linear-gradient(160deg,#7fb0a8,#8b7a35 35%,#5d5228 70%,#3b3a30)"><h3 class="tile-title" style="left:13px">Lorem ipsum dolor</h3><p class="tile-meta" style="left:13px">7 PHOTOS<span>•</span>21 OCT 2016</p></article>
    <article class="tile" role="img" aria-label="Bride and groom holding hands facing a sunset sea" style="background:linear-gradient(180deg,#1f1d1c,#b87a3a 35%,#3a3230 60%,#7a5a40)"><h3 class="tile-title" style="left:13px">Lorem ipsum dolor</h3><p class="tile-meta" style="left:13px">7 PHOTOS<span>•</span>21 OCT 2016</p></article>
    <article class="tile" role="img" aria-label="Bouquet of pink roses with a gift box" style="background:linear-gradient(135deg,#2d3550,#e07a80 40%,#b5646a 65%,#3c3a40)"><h3 class="tile-title">Lorem ipsum dolor</h3><p class="tile-meta">7 PHOTOS<span>•</span>21 OCT 2016</p></article>
    <article class="tile" role="img" aria-label="Girl in a light dress in a flower meadow" style="background:linear-gradient(160deg,#5f8ab0,#8aa870 45%,#b9b070 75%,#5a7a38)"><h3 class="tile-title" style="left:19px">Lorem ipsum dolor</h3><p class="tile-meta" style="left:19px">7 PHOTOS<span>•</span>21 OCT 2016</p></article>
    <article class="tile" role="img" aria-label="Pink roses beside a lantern and a compass" style="background:linear-gradient(135deg,#9ea4a0,#c27aa8 35%,#6a7a62 65%,#3a3f3a)"><h3 class="tile-title" style="left:13px;bottom:40px">Lorem ipsum dolor</h3><p class="tile-meta" style="left:13px;bottom:24px">7 PHOTOS<span>•</span>21 OCT 2016</p></article>
    <article class="tile" role="img" aria-label="Small child in a white coat on a cobbled path" style="background:linear-gradient(160deg,#4a4a2e,#6a6a40 45%,#8a8a78 70%,#3a3a28)"><h3 class="tile-title">Lorem ipsum dolor</h3><p class="tile-meta">7 PHOTOS<span>•</span>21 OCT 2016</p></article>
    <article class="tile" role="img" aria-label="Small glass bottle with a pink ribbon bow" style="background:linear-gradient(160deg,#c9b48a,#9aa870 40%,#5e8a6a 70%,#2f4a3a)"><h3 class="tile-title" style="left:19px">Lorem ipsum dolor</h3><p class="tile-meta" style="left:19px">7 PHOTOS<span>•</span>21 OCT 2016</p></article>
    <article class="tile" role="img" aria-label="Woman posing in a teal-lit vintage bedroom" style="background:linear-gradient(135deg,#1a6a9a,#2d8ab0 40%,#c9a890 65%,#2a5a7a)"><h3 class="tile-title" style="left:13px">Lorem ipsum dolor</h3><p class="tile-meta" style="left:13px">7 PHOTOS<span>•</span>21 OCT 2016</p></article>
    <article class="tile" role="img" aria-label="Cherry blossom trees along a green riverbank" style="background:linear-gradient(160deg,#2a2a25,#c9a2a8 35%,#6aa030 65%,#3a7a20)"><h3 class="tile-title">Lorem ipsum dolor</h3><p class="tile-meta">7 PHOTOS<span>•</span>21 OCT 2016</p></article>
    <article class="tile" role="img" aria-label="Woman sitting on rocks at dusk" style="background:linear-gradient(160deg,#2a3a6a,#4a5a8a 40%,#8a8a9a 60%,#2a2e40)"><h3 class="tile-title" style="left:19px">Lorem ipsum dolor</h3><p class="tile-meta" style="left:19px">7 PHOTOS<span>•</span>21 OCT 2016</p></article>
    <article class="tile" role="img" aria-label="Glowing butterflies flying out of a jar at night" style="background:radial-gradient(ellipse at 60% 55%,#6a6030,#1a1a14 55%,#0c0c0a)"><h3 class="tile-title" style="left:13px">Lorem ipsum dolor</h3><p class="tile-meta" style="left:13px">7 PHOTOS<span>•</span>21 OCT 2016</p></article>
  </section>

  <p class="label" style="top:1146px">LET'S WORKS TOGETHER</p>
  <p class="collab-text">Lorem ipsum dolor sit amet consectetur adipiscing elit. Aliquam venenatis nibh vitae consequat auctor. Ali<br>quam sed lorem tristique nisl egestas sollicitudin. Duis pulvinar vitae purus sed luctus Nulla aliquet</p>
  <a class="btn">CONTACTS ME</a>

  <footer class="footer">
    <div class="col" style="left:47px;width:140px">
      <h4>POPULAR POSTS</h4>
      <div class="post"><div class="thumb" role="img" aria-label="Post photo" style="background:linear-gradient(135deg,#5a9a50,#c0506a)"></div><p class="post-title">Lorem ipsum dolor sit</p><p class="post-date">20THOCT 2016</p></div>
      <div class="post"><div class="thumb" role="img" aria-label="Post photo" style="background:linear-gradient(135deg,#8aa0b0,#c83a6a)"></div><p class="post-title">Lorem ipsum dolor sit</p><p class="post-date">20THOCT 2016</p></div>
      <div class="post"><div class="thumb" role="img" aria-label="Post photo" style="background:linear-gradient(180deg,#3a7ac0,#e0b030)"></div><p class="post-title">Lorem ipsum dolor sit</p><p class="post-date">20THOCT 2016</p></div>
    </div>
    <div class="col" style="left:207px;top:36px">
      <h4>TOP CATEGORIES</h4>
      <ul class="cats">
        <li>Lifestyle (21)</li><li>Photography (19)</li><li>Journal (16)</li><li>Works (7)</li>
        <li>Lifestyle (21)</li><li>Photography (19)</li><li>Journal (16)</li><li>Works (7)</li>
      </ul>
    </div>
    <div class="col contact" style="left:367px">
      <h4>GET IN TOUCH</h4>
      <p>Tebani Studio Ltd.</p>
      <p>Harrow Lane Studios, 22/B</p>
      <p>London, LN 40217</p>
      <p>P: (020) 555-0148</p>
      <p>E: hello@tebanistudio.example</p>
      <h4 style="margin-top:16px;margin-bottom:4px">FOLLOW US</h4>
      <div class="social">
        <i style="background:#e8741c"></i><i style="background:#3aa0d8"></i><i style="background:#3a5aa8"></i><i style="background:#c8202a"></i><i style="background:#1a80b8"></i><i style="background:#3a8a3a"></i>
      </div>
    </div>
    <div class="col" style="left:528px">
      <h4>ABOUT ME</h4>
      <div class="about-photo" role="img" aria-label="Photographer holding a camera in dim light"></div>
      <p class="about-text">Lorem ipsum dolor sit amet, consectetur adipiscing elit. Aliquam venenatis nibh vitae consequat auctor. Aliqu</p>
    </div>
    <p class="copyright">Copyright © 2016. All Rights Reserved</p>
  </footer>

</main>
</div>
</body>
</html>
```